WWW.VELTRONA.IT BUSINNES CARD

WE NEED A BUSINESS CARD . I HAVE A COMPANY IN ITALY NR 1 IN HAIR MEDICAL CARE AN HAIR REPLECEMENT . IN CARD I NEED WRITE WEB ADDRESS, MAIL , ADDRESS, TELEPHONE NUMBER , AND NAME
IN THE BACK SIDE I NEED MY DOCTOR LOGO .
MY WEB SITE IS WWW.VELTRONA.IT
Updates

Target Market(s)

CONSUMER B2C

Industry/Entity Type

Hair And Beauty

Contact Information for Business Card

I WANT A MEDICAL BUSINESS CARD.

Font styles to use
Other font styles liked:
• VERDANA

Colors
33a6d7
3176b5
85abd2
aedbee
eaf1f7
ffffff

Requirements
Must have
• I NEED MY LOGO AND LOGO OF DR VELTRONA

```html
<!DOCTYPE html>
<html lang="it">
<head>
<meta charset="utf-8">
<title>Veltrona – biglietto da visita</title>
<link rel="stylesheet" href="https://fonts.googleapis.com/css2?family=Noto+Sans:wght@400;700&family=Open+Sans:wght@400;700&display=swap">
<style>
  :root{
    --sky:#33a6d7;
    --sky-bright:#2fb5e6;
    --blue:#3176b5;
    --navy:#0a559a;
    --pale:#eaf1f7;
    --ink:#333333;
    --white:#ffffff;
    --skin:#f3b899;
    --hair:#6b3a1f;
  }
  *{margin:0;padding:0;box-sizing:border-box}
  html,body{width:1200px;height:1200px;overflow:hidden;background:var(--white)}
  body{position:relative;font-family:"Noto Sans",Verdana,sans-serif}

  .card{position:absolute;left:296px;width:608px;height:428px;border:1px solid var(--blue);background:var(--white);overflow:hidden}
  .card--front{top:85px}
  .card--back{top:682px}
  .card__bg{position:absolute;left:0;top:0;width:100%;height:100%}

  /* front */
  .brand{position:absolute;left:0;right:0;top:62px;display:flex;align-items:center;justify-content:center;gap:22px}
  .brand__mark{width:72px;height:72px;background:var(--sky)}
  .brand__name{font-family:"Open Sans",Verdana,sans-serif;font-weight:700;font-size:88px;line-height:1;color:var(--navy);letter-spacing:-1px}
  .tagline{position:absolute;left:0;right:0;top:172px;text-align:center;font-family:"Open Sans",Verdana,sans-serif;font-size:22px;letter-spacing:.5px;color:var(--navy)}
  .website{position:absolute;left:0;right:0;top:302px;text-align:center;font-weight:700;font-size:28px;color:var(--navy)}
  .branches{position:absolute;top:348px;left:0;width:100%}
  .branch{position:absolute;top:0;font-size:17px;line-height:22px;color:var(--ink)}
  .branch__city{font-weight:700;font-size:18px;color:var(--blue)}
  .branch--firenze{left:37px}
  .branch--livorno{left:242px}
  .branch--verona{left:438px}

  /* back */
  .services{position:absolute;left:23px;top:21px;list-style:none;font-weight:700;font-size:21px;line-height:25.7px;color:var(--navy)}
  .mascot{position:absolute;left:408px;top:30px;width:190px;height:370px}
  .mascot__area{position:absolute;left:0;top:0;width:100%;height:100%}
  .doctor-name{position:absolute;left:515px;top:290px;transform:rotate(-90deg);transform-origin:left top;font-weight:700;font-size:22px;color:var(--navy);white-space:nowrap}
</style>
</head>
<body>

<section class="card card--front">
  <svg class="card__bg" viewBox="0 0 608 428" aria-hidden="true">
    <path d="M0 428 V318 C120 275 260 280 400 292 C480 298 560 290 608 278 V428 Z" fill="var(--pale)"/>
    <path d="M0 308 C40 275 95 262 135 262 C90 266 40 282 0 308 Z M0 310 L0 290 C30 270 80 260 135 262 C80 266 35 285 0 310 Z" fill="var(--blue)"/>
    <path d="M25 252 C120 225 220 228 330 252 C430 272 520 258 585 218 C530 262 440 285 330 262 C220 240 120 236 25 252 Z" fill="var(--sky-bright)"/>
    <path d="M470 276 C530 270 575 255 608 228 V258 C570 272 525 278 470 276 Z" fill="var(--blue)"/>
  </svg>

  <div class="brand">
    <span class="brand__mark"></span>
    <span class="brand__name">Veltrona</span>
  </div>
  <p class="tagline">CURA E REINTEGRAZIONE DEI CAPELLI</p>

  <p class="website">www.veltrona.it</p>

  <div class="branches">
    <address class="branch branch--firenze" style="font-style:normal">
      <div class="branch__city">Firenze</div>
      <div>via dei Tigli 42/8</div>
      <div>tel 055 4120 736</div>
    </address>
    <address class="branch branch--livorno" style="font-style:normal">
      <div class="branch__city">Livorno</div>
      <div>via dei Mulini 117</div>
      <div>tel 0586 731290</div>
    </address>
    <address class="branch branch--verona" style="font-style:normal">
      <div class="branch__city">Verona</div>
      <div>via Castello 15</div>
      <div>tel 045 803417</div>
    </address>
  </div>
</section>

<section class="card card--back">
  <svg class="card__bg" viewBox="0 0 608 428" aria-hidden="true">
    <path d="M0 335 C120 370 300 372 430 340 C500 322 560 290 608 276 V428 H0 Z" fill="var(--pale)"/>
  </svg>

  <ul class="services">
    <li>- consulenza</li>
    <li>- check-up</li>
    <li>- hairtest</li>
    <li>- trattamenti e prodotti tricologici</li>
    <li>- stimolazione delle cellule staminali</li>
    <li>- autotrapianto fue</li>
    <li>- fotostimolazione</li>
    <li>- ossigenoterapia</li>
    <li>- parrucche medicali</li>
    <li>- soluzione invisibili</li>
    <li>- infoltimento naturale</li>
  </ul>

  <div class="mascot">
    <svg class="mascot__area" viewBox="0 0 190 370" role="img" aria-label="Mascotte del dottore Veltrona: un capello sorridente in camice bianco">
      <defs>
        <linearGradient id="mascotTone" x1="0" y1="0" x2="0" y2="1">
          <stop offset="0" stop-color="var(--hair)"/>
          <stop offset=".75" stop-color="#9a6a4a"/>
          <stop offset="1" stop-color="var(--skin)"/>
        </linearGradient>
      </defs>
      <rect x="40" y="0" width="110" height="345" rx="30" fill="url(#mascotTone)" opacity=".85"/>
      <ellipse cx="92" cy="345" rx="93" ry="20" fill="var(--skin)"/>
    </svg>
  </div>
  <div class="doctor-name">dr. Veltrona</div>
</section>

</body>
</html>
```